Website Needs a New Look & Feel - I am Too Old and Uncool on my Own

I want some design ideas for my current site. I need a new, more modern and dynamic look and feel. The audience for the site is 90% male, 24-54 years old, and not highly educated. English is second language for about 30% of audience, so images help. 85% of visitors view on mobile. We sell trucks and trailers to this audience. . Just want something new and cool. Tired of what I have. Current site doesn't seem strong enough to match the kind of people who drive trucks for a living. Current is site is brelvon.com. Pull relevant menu and text from the site.

Target Market(s)

Truck Drivers and Trucking Company Owners (90% male).

Industry/Entity Type

Transportation - Specifically, truck and trailer sales.

Number of Pages Required

3 page

Font styles to use
Sans Serif

Colors
0054AA
0677BA
7BADD7
CADEEF
E8F1F8

Requirements
Must have
• Images of Sleeper Trucks (like on there now) and trailers. Audience is very literal, so they need to see what we sell.
Nice to have
• Images of Sleeper Trucks (like on tMy inventory pages are boring, please show me something more user-friendly and interesting. here now) and trailers.

```html
<!DOCTYPE html>
<html lang="en">
<head>
<meta charset="utf-8">
<title>Brelvon Truck &amp; Trailer</title>
<link href="https://fonts.googleapis.com/css2?family=Lexend:wght@300;400;500;600;700&display=swap" rel="stylesheet">
<style>
:root{
  --blue:#1d4fb8;
  --blue-dark:#0054aa;
  --ink:#1b1b1d;
  --text:#3d3e42;
  --grey:#5b5c61;
  --grey-dark:#46474b;
  --grey-light:#ececee;
  --white:#ffffff;
}
*{margin:0;padding:0;box-sizing:border-box}
html,body{width:1200px;height:4866px;overflow:hidden}
body{font-family:"Lexend",sans-serif;color:var(--text);background:var(--white);position:relative}
.abs{position:absolute}
.photo{position:absolute}
.btn{position:absolute;height:40px;border-radius:20px;display:flex;align-items:center;padding:0 6px 0 20px;font-size:12px;font-weight:500;text-transform:uppercase;gap:14px;justify-content:space-between}
.btn .arr{width:28px;height:28px;border-radius:50%;display:flex;align-items:center;justify-content:center}
.btn-blue{background:var(--blue);color:#fff}
.btn-blue .arr{background:#fff}
.btn-white{background:#fff;color:var(--blue)}
.btn-white .arr{background:var(--blue)}
.btn-grey{background:var(--grey);color:#fff}
.btn-grey .arr{background:#fff}
.logo{position:absolute;font-weight:700;color:var(--ink);line-height:1}
.logo .big{font-size:44px;letter-spacing:-1px}
.logo .small{font-size:20px;font-weight:700;margin-top:-2px}

/* header */
.topbar{position:absolute;left:370px;top:0;width:830px;height:32px;background:#5e5f64;clip-path:polygon(22px 0,100% 0,100% 100%,0 100%)}
.topbar .item{position:absolute;top:8px;font-size:11px;color:#fff;display:flex;align-items:center;gap:8px}
.ico-c{width:20px;height:20px;border-radius:50%;background:#fff;display:inline-block}
.nav{position:absolute;top:52px;left:384px;display:flex;gap:22px;font-size:12px;color:#666;text-transform:uppercase}
.nav .on{color:var(--blue)}
/* hero */
.hero{position:absolute;left:0;top:85px;width:1200px;height:645px;background:linear-gradient(100deg,#141518 0%,#2c2f36 35%,#6a6660 60%,#a08a6c 80%,#cfae80 100%)}
.hero h1{position:absolute;left:144px;top:92px;color:#fff;font-size:41px;font-weight:500;line-height:54px;text-transform:uppercase;width:400px}
.hero p{position:absolute;left:144px;top:265px;color:#fff;font-size:14px;line-height:23px;width:320px;padding-left:10px;border-left:3px solid var(--blue)}
/* stats */
.stat{position:absolute;top:800px;width:220px;text-align:center}
.stat b{display:block;font-size:42px;font-weight:600;color:var(--ink)}
.stat span{font-size:13px;text-transform:uppercase;color:var(--ink)}
.vline{position:absolute;top:812px;width:2px;height:62px;background:#ddd}
.h2{position:absolute;left:0;width:1200px;text-align:center;font-size:31px;font-weight:500;color:var(--ink);text-transform:uppercase}
.h2 em{font-style:normal;color:var(--blue);font-weight:600}
.lead{position:absolute;text-align:center;font-size:12px;line-height:22px;color:var(--text)}
.card{position:absolute;top:1098px;width:240px}
.card .pic{height:246px}
.card h3{margin-top:22px;margin-left:5px;font-size:14px;font-weight:600;text-transform:uppercase;color:var(--ink)}
.card p{margin:8px 5px 0;font-size:11.5px;line-height:20px}
.more{display:inline-block;margin:12px 5px 0;font-size:12px;color:var(--blue);border-bottom:1px solid var(--blue);padding-bottom:1px}
/* wholesale */
.whole{position:absolute;left:0;top:1565px;width:1200px;height:520px}
.whole h2{position:absolute;left:646px;top:90px;font-size:31px;font-weight:500;line-height:43px;color:#fff;text-transform:uppercase;width:520px}
.whole h2 b{font-weight:600}
.whole p{position:absolute;left:646px;top:182px;width:400px;font-size:12.5px;line-height:23px;color:#fff}
/* prices */
.pcard{position:absolute;top:2332px;width:283px;height:268px;text-align:center}
.pcard .ic{width:82px;height:82px;border-radius:50%;margin:30px auto 0;display:flex;align-items:center;justify-content:center}
.pcard h3{margin-top:28px;font-size:17px;font-weight:600;text-transform:uppercase;color:var(--ink)}
.pcard p{margin:14px auto 0;width:220px;font-size:12.5px;line-height:22px}
/* buying */
.buy h2{position:absolute;left:142px;top:2748px;font-size:31px;font-weight:500;line-height:44px;text-transform:uppercase;color:var(--ink)}
.buy h2 b{color:var(--blue);font-weight:600}
.buy p{position:absolute;left:142px;width:430px;font-size:12.5px;line-height:22.5px}
/* faq */
.fcard{position:absolute;top:3814px;width:287px}
.fcard .pic{height:250px}
.fcard .date{margin:22px 8px 0;font-size:11px;color:var(--blue)}
.fcard h3{margin:8px 8px 0;font-size:14px;font-weight:600;line-height:22px;text-transform:uppercase;color:var(--ink)}
.fcard p{margin:10px 8px 0;font-size:11.5px;line-height:20px}
.fcard .more{margin:18px 8px 0}
/* footer */
.foot{position:absolute;left:0;top:4400px;width:1200px;height:466px}
.fcol{position:absolute;top:4572px;padding-left:18px;border-left:2px solid #fff;color:#fff}
.fcol h4{font-size:14px;font-weight:500;margin-bottom:16px}
.fcol li{list-style:none;font-size:11.5px;line-height:29px}
.copy{position:absolute;left:0;top:4829px;width:1200px;height:37px;background:#3a3b3e;color:#fff;font-size:11px;text-align:center;line-height:37px}
</style>
</head>
<body>

<!-- header -->
<div class="logo" style="left:140px;top:12px"><div class="big">BRELVON</div><div class="small">Truck &amp; Trailer</div></div>
<div class="topbar">
  <div class="item" style="left:60px"><span class="ico-c"></span>Call Us Today: <b>555-014-2290</b></div>
  <div class="item" style="left:288px"><span class="ico-c"></span>Email Us: <b>info@brelvon.com</b></div>
  <div class="item" style="left:570px;gap:6px"><span class="ico-c"></span><span class="ico-c"></span><span class="ico-c"></span><span class="ico-c"></span></div>
</div>
<nav class="nav"><span class="on">Sleepers</span><span>Reefers</span><span>Dry Vans</span><span>Cranes</span><span>Resources</span><span>Contact Us</span></nav>
<div class="btn btn-blue" style="left:882px;top:43px;height:32px;width:178px;font-size:11px;padding-left:14px"><span>See Our Inventory</span><span class="arr" style="width:22px;height:22px"><svg width="10" height="10" viewBox="0 0 10 10"><path d="M2 2l3 3-3 3M5 2l3 3-3 3" stroke="#1d4fb8" stroke-width="1.4" fill="none"/></svg></span></div>

<!-- hero -->
<section class="hero">
  <div class="photo" role="img" aria-label="Blue sleeper semi truck with white trailer on highway at sunset" style="left:520px;top:30px;width:680px;height:480px;background:radial-gradient(ellipse at 45% 55%,#2c4f9c 0%,#3d5a8a 30%,rgba(90,90,100,0.4) 60%,rgba(0,0,0,0) 75%)"></div>
  <h1>Built for a long haul prices to move for you</h1>
  <p>We sell dependable sleeper trucks &amp; trailers to drivers across the U.S. Sleeper trucks and trailers built for uptime and profit.</p>
  <div class="btn btn-blue" style="left:144px;top:370px;width:204px"><span>See Our Inventory</span><span class="arr"><svg width="12" height="12" viewBox="0 0 10 10"><path d="M2 2l3 3-3 3M5 2l3 3-3 3" stroke="#1d4fb8" stroke-width="1.4" fill="none"/></svg></span></div>
  <div class="btn btn-white" style="left:364px;top:370px;width:124px"><span>Call Us</span><span class="arr"><svg width="12" height="12" viewBox="0 0 10 10"><path d="M2 2l3 3-3 3M5 2l3 3-3 3" stroke="#fff" stroke-width="1.4" fill="none"/></svg></span></div>
  <svg class="abs" style="left:0;top:535px" width="1200" height="115" viewBox="0 0 1200 115"><polygon points="0,30 1200,110 1200,115 0,115" fill="#d4d4d6"/><polygon points="0,64 1200,112 1200,115 0,115" fill="#fff"/></svg>
</section>

<!-- stats -->
<div class="stat" style="left:55px"><b>20+</b><span>Year of Experience</span></div>
<div class="vline" style="left:308px"></div>
<div class="stat" style="left:337px"><b>5,300+</b><span>Vehicles Sold</span></div>
<div class="vline" style="left:588px"></div>
<div class="stat" style="left:628px"><b>$250M+</b><span>In Transactions</span></div>
<div class="vline" style="left:890px"></div>
<div class="stat" style="left:922px"><b>98%</b><span>Client Satisfaction</span></div>

<!-- what we offer -->
<div class="h2" style="top:975px">What we <em>offer</em></div>
<div class="lead" style="left:200px;top:1024px;width:800px">Lorem ipsum dolor sit amet, consectetur adipiscing elit, sed do eiusmod tempor incididunt ut labore et dolore magna aliqua. Ut enim ad minim veniam, quis nostrud exercitation ullamco laboris nisi ut aliquip</div>
<div class="card" style="left:94px"><div class="pic" role="img" aria-label="White reefer trailer with refrigeration unit" style="background:linear-gradient(180deg,#7e97b1,#d8dde2 60%,#8a8c8f)"></div><h3>Reefer Trailers</h3><p>Lorem ipsum dolor sit, consectetur on adipiscing elit, sed do eiusmod tempor incididunt ut labore et dolore.</p><span class="more">Read More »</span></div>
<div class="card" style="left:351px"><div class="pic" role="img" aria-label="White sleeper truck parked on road" style="background:linear-gradient(180deg,#c9d6e2,#e8ecef 55%,#6f7d6e)"></div><h3>Sleepers</h3><p>Lorem ipsum dolor sit, consectetur on adipiscing elit, sed do eiusmod tempor incididunt ut labore et dolore.</p><span class="more">Read More »</span></div>
<div class="card" style="left:608px"><div class="pic" role="img" aria-label="White dry van trailer" style="background:linear-gradient(180deg,#c5a58a,#e9e8e5 50%,#7d7b78)"></div><h3>Dry Vans</h3><p>Lorem ipsum dolor sit, consectetur on adipiscing elit, sed do eiusmod tempor incididunt ut labore et dolore.</p><span class="more">Read More »</span></div>
<div class="card" style="left:865px"><div class="pic" role="img" aria-label="Yellow mobile crane truck" style="background:linear-gradient(180deg,#7fa6d3,#e7c23a 55%,#6b6454)"></div><h3>Cranes</h3><p>Lorem ipsum dolor sit, consectetur on adipiscing elit, sed do eiusmod tempor incididunt ut labore et dolore.</p><span class="more">Read More »</span></div>

<!-- wholesale -->
<section class="whole">
  <svg class="abs" style="left:0;top:0" width="1200" height="520" viewBox="0 0 1200 520"><polygon points="0,0 1200,0 1200,425 0,510" fill="#4a4b4f"/></svg>
  <div class="photo" role="img" aria-label="Warehouse and trucks background" style="left:0;top:0;width:640px;height:510px;background:linear-gradient(90deg,rgba(40,40,44,0.6),rgba(74,75,79,0));clip-path:polygon(0 0,100% 0,100% 82%,0 100%)"></div>
  <div class="photo" role="img" aria-label="Aerial view of white semi trailer truck driving on highway" style="left:136px;top:75px;width:469px;height:516px;background:linear-gradient(160deg,#9a9b9b,#d9d9d6 45%,#b2b4b3);border:6px solid #fff"></div>
  <h2>Wholesale reefers, dry <b>vans and sleepers</b></h2>
  <p>Brelvon Truck &amp; Trailer is an equipment dealership in Kansas City, offering wholesale reefers, dry vans, and sleepers at the best prices. We aren't a dealership, because you can buy directly from us at wholesale price &amp; save thousands. We don't have a fancy sales lot, but do  prices on good, clean equipment in the country.</p>
  <div class="btn btn-white" style="left:646px;top:325px;width:206px"><span>See Our Inventory</span><span class="arr"><svg width="12" height="12" viewBox="0 0 10 10"><path d="M2 2l3 3-3 3M5 2l3 3-3 3" stroke="#fff" stroke-width="1.4" fill="none"/></svg></span></div>
</section>

<!-- prices -->
<div class="h2" style="top:2262px">How are the prices <em>so low?</em></div>
<div class="pcard" style="left:140px"><div class="ic" style="background:#5b5c61;border:4px solid #e2e2e4"><svg width="40" height="40" viewBox="0 0 40 40" fill="none" stroke="#fff" stroke-width="2.5"><path d="M8 32L24 16M26 8a6 6 0 0 1 6 6l-4 1-3-3 1-4z"/><path d="M32 32L16 16M10 8l4 4-2 2-4-4"/></svg></div><h3>Huge Equipment</h3><p>We buy huge packages of equipment, 100+ at a time, so we get a great price on what we buy.</p></div>
<div class="pcard" style="left:459px;background:#5b5c61;color:#fff"><div class="ic" style="background:#fff;border:4px solid #8a8b90"><svg width="40" height="40" viewBox="0 0 40 40" fill="none" stroke="#5b5c61" stroke-width="2.5"><circle cx="18" cy="18" r="11"/><path d="M18 11v14M22 14h-5a2.5 2.5 0 0 0 0 5h2a2.5 2.5 0 0 1 0 5h-5M30 26v8M26 30l4 4 4-4"/></svg></div><h3 style="color:#fff">Overhead Cost</h3><p>We don't operate a big retail sales lot, so we don't have all that overhead cost</p></div>
<div class="pcard" style="left:777px"><div class="ic" style="background:#5b5c61;border:4px solid #e2e2e4"><svg width="40" height="40" viewBox="0 0 40 40" fill="none" stroke="#fff" stroke-width="2.5"><circle cx="20" cy="17" r="10"/><path d="M20 11v12M23 13.5h-4a2 2 0 0 0 0 4h2a2 2 0 0 1 0 4h-4M14 26l-4 8 5-1 2 4 3-7M26 26l4 8-5-1-2 4-3-7"/></svg></div><h3>Lower Profit</h3><p>We sell at a lower profit margin, and make it up by selling a lot more equipment.</p></div>

<!-- buying -->
<section class="buy">
  <svg class="abs" style="left:560px;top:2580px" width="640" height="620" viewBox="0 0 640 620"><polygon points="640,0 640,150 380,150" fill="#1d4fb8"/><polygon points="340,380 640,380 640,620" fill="#1d4fb8"/></svg>
  <div class="photo" role="img" aria-label="White sleeper semi truck, front three-quarter view" style="left:605px;top:2715px;width:595px;height:370px;background:radial-gradient(ellipse at 55% 50%,#f4f5f6 0%,#d9dbdd 45%,#a8abaf 65%,rgba(255,255,255,0) 72%)"></div>
  <h2>Buying from Brelvon Truck<br><b>and trailer</b></h2>
  <p style="top:2845px">When you buy from Brelvon, you are buying at a “wholesale price.” In other words, you pay the same price a truck dealer pays when they buy from us. We guarantee that you won't find a better price on the same truck or trailer anywhere in the U.S.</p>
  <p style="top:2945px">As one of the leading equipment dealerships in the U.S., Brelvon Truck &amp; Trailer is committed to going the extra mile. We believe that offering the best quality equipment at the lowest prices isn't enough. We strive to exceed your expectations by providing the highest level of service from start to finish—no sales talk or runaround.</p>
</section>

<!-- equipment band -->
<div class="photo" role="img" aria-label="Row of parked semi trucks, faded" style="left:0;top:3203px;width:1200px;height:420px;background:linear-gradient(180deg,#dfe3e8,#c8cfd6 50%,#e4e7ea)"></div>
<div class="abs" style="left:0;top:3203px;width:1200px;height:420px;background:rgba(255,255,255,0.55)"></div>
<div class="h2" style="top:3345px;font-size:33px;line-height:48px">You have more <em>equipment</em><br><em>than you need?</em></div>
<div class="lead" style="left:200px;top:3440px;width:800px">Find dependable sleeper trucks and trailers that earn their keep We help drivers and fleets find the right equipment fast.</div>
<div class="btn btn-blue" style="left:360px;top:3498px;width:232px"><span>Sell Your Equipment</span><span class="arr"><svg width="12" height="12" viewBox="0 0 10 10"><path d="M2 2l3 3-3 3M5 2l3 3-3 3" stroke="#1d4fb8" stroke-width="1.4" fill="none"/></svg></span></div>
<div class="btn btn-grey" style="left:606px;top:3498px;width:232px"><span>Call Us: 555-014-2290</span><span class="arr"><svg width="12" height="12" viewBox="0 0 10 10"><path d="M2 2l3 3-3 3M5 2l3 3-3 3" stroke="#5b5c61" stroke-width="1.4" fill="none"/></svg></span></div>

<!-- faq -->
<div class="h2" style="top:3716px">Frequently asked <em>questions?</em></div>
<div class="lead" style="left:150px;top:3764px;width:900px">Lorem ipsum dolor sit amet, consectetur adipiscing elit, sed do eiusmod tempor incididunt ut labore et dolore magna aliqua.</div>
<div class="fcard" style="left:142px"><div class="pic" role="img" aria-label="Blue trucks parked at loading docks" style="background:linear-gradient(180deg,#6d9bd6,#e5e9ee 45%,#2d55a8 75%,#888)"></div><div class="date">July 22, 2025</div><h3>Transform your trucking experience with an APU!</h3><p>“Think about how an APU could change your trucking experience for the better!” Long hauls can be tough, especially when it comes to finding a...</p><span class="more">Read More »</span></div>
<div class="fcard" style="left:456px"><div class="pic" role="img" aria-label="White truck on mountain highway" style="background:linear-gradient(180deg,#aebfd0,#6f8069 45%,#9a9e98)"></div><div class="date">July 22, 2025</div><h3>Why Highway Cruiser's are the better choice</h3><p>When it comes to choosing the right truck for your hauling needs, the decision can feel overwhelming. With so many options on the market, it's</p><span class="more">Read More »</span></div>
<div class="fcard" style="left:771px"><div class="pic" role="img" aria-label="Yellow crane at construction site" style="background:linear-gradient(180deg,#b9cde3,#d8b43c 50%,#5e5a4c)"></div><div class="date">July 22, 2025</div><h3>On the other hand we are in denounce</h3><p>When it comes to choosing the right truck for your hauling needs, the decision can feel overwhelming. With so many options on the market, it's</p><span class="more">Read More »</span></div>
<svg class="abs" style="left:568px;top:4304px" width="64" height="10" viewBox="0 0 64 10"><circle cx="5" cy="5" r="4" fill="#ccc"/><circle cx="21" cy="5" r="4" fill="#1d4fb8"/><circle cx="37" cy="5" r="4" fill="#ccc"/><circle cx="53" cy="5" r="4" fill="#ccc"/></svg>

<!-- footer -->
<footer class="foot">
  <svg class="abs" style="left:0;top:0" width="1200" height="466" viewBox="0 0 1200 466"><polygon points="0,50 1200,50 1200,466 0,466" fill="#4a4b4f"/><polygon points="0,-140 140,50 0,240" fill="#1d4fb8"/><polygon points="0,20 110,50 0,210" fill="#0054aa"/></svg>
</footer>
<div class="logo" style="left:140px;top:4560px;color:#fff"><div class="big">BRELVON</div><div class="small">Truck &amp; Trailer</div></div>
<p class="abs" style="left:140px;top:4640px;width:250px;font-size:11.5px;line-height:20px;color:#fff">Lorem ipsum dolor sit amet, consectetur adipiscing elit, sed do eiusmod tempor incididunt ut labore et magna aliqua.</p>
<div class="abs" style="left:140px;top:4732px;display:flex;align-items:center;gap:10px;color:#fff;font-size:11.5px">Follow Us: <span class="ico-c" style="width:28px;height:28px;background:transparent;border:2px solid #fff"></span><span class="ico-c" style="width:28px;height:28px"></span><span class="ico-c" style="width:28px;height:28px;background:transparent;border:2px solid #fff"></span></div>
<div class="fcol" style="left:461px"><h4>Quick Links</h4><ul><li>Sleepers</li><li>Reefers</li><li>Dry Vans</li><li>Cranes</li><li>Resources</li><li>Contact Us</li></ul></div>
<div class="fcol" style="left:652px"><h4>Services</h4><ul><li>Reefer Trailers</li><li>Sleepers</li><li>Dry Vans</li><li>Cranes</li></ul></div>
<div class="fcol" style="left:843px;height:220px"><h4>Contact Us</h4>
  <div style="display:flex;gap:14px;align-items:flex-start;font-size:11.5px;line-height:22px"><span class="ico-c" style="width:30px;height:30px;flex:none;display:flex;align-items:center;justify-content:center"><svg width="14" height="14" viewBox="0 0 14 14"><path d="M7 1a4 4 0 0 1 4 4c0 3-4 8-4 8S3 8 3 5a4 4 0 0 1 4-4z" fill="#4a4b4f"/><circle cx="7" cy="5" r="1.5" fill="#fff"/></svg></span><span>123, Lorem ipsum dolor sit<br>amet, consectetur - 52100</span></div>
  <div style="display:flex;gap:14px;align-items:center;font-size:11.5px;margin-top:14px"><span class="ico-c" style="width:30px;height:30px;display:flex;align-items:center;justify-content:center"><svg width="14" height="14" viewBox="0 0 14 14"><path d="M3 1l2.5 3-1.5 1.5a8 8 0 0 0 4.5 4.5L10 8.5l3 2.5-1.5 2C6 13 1 8 1 2.5z" fill="#4a4b4f"/></svg></span>Call Us: 555-014-2290</div>
  <div style="display:flex;gap:14px;align-items:center;font-size:11.5px;margin-top:18px"><span class="ico-c" style="width:30px;height:30px;background:transparent;display:flex;align-items:center;justify-content:center"><svg width="18" height="14" viewBox="0 0 18 14"><rect x="1" y="1" width="16" height="12" rx="1" fill="#fff"/><path d="M1 2l8 6 8-6" stroke="#4a4b4f" fill="none"/></svg></span>info@brelvon.com</div>
</div>
<div class="copy">@copyright 2026 Brelvon &nbsp;||&nbsp; Privacy Policy</div>

</body>
</html>
```